Creative Stationary for Solo Law Firm

I am looking for stationary designs for my solo law firm called TM Halvorsen Law PLLC. My logo is attached. I'd like the logo incorporated into the design.

I'm looking for a stationary design that is a bit outside of the box and not too standard or boring. The final design should communicate professionalism.

Target Market(s)

United States Clients, Opposing Counsel

Industry/Entity Type

Legal

Font styles to use
Sans Serif

Requirements
Must have
• The stationary design must incorporate my logo design attached. The design itself must be creative. The envelope design must follow standard United States designs with room for the postage stamp at the top right corner and space for the recipient's address in the middle.

```html
<!DOCTYPE html>
<html lang="en">
<head>
<meta charset="utf-8">
<title>TM Halvorsen Law PLLC — Stationery</title>
<link rel="stylesheet" href="https://fonts.googleapis.com/css2?family=Open+Sans:wght@400;600&display=swap">
<style>
  :root {
    --navy: #232c74;
    --grey: #cfd0d4;
    --paper: #ffffff;
    --ink: #2b2b33;
    --muted: #6a6c78;
    --backdrop: #e7e8eb;
  }
  * { box-sizing: border-box; margin: 0; padding: 0; }
  html, body { width: 1200px; height: 2668px; overflow: hidden; }
  body {
    background: var(--backdrop);
    font-family: "Open Sans", sans-serif;
    color: var(--ink);
    display: flex;
    flex-direction: column;
    align-items: center;
    justify-content: center;
    gap: 150px;
  }
  .row { display: flex; gap: 40px; }

  .piece {
    position: relative;
    background: var(--paper);
    overflow: hidden;
    box-shadow: 0 6px 18px rgba(20, 24, 50, 0.12);
  }
  .content { position: relative; z-index: 1; }

  /* Placeholder area for the decorative ornament */
  .ornament-area { position: absolute; }
  .ornament-area.horizontal { background: linear-gradient(180deg, var(--grey) 0%, var(--navy) 100%); }
  .ornament-area.vertical { background: linear-gradient(90deg, var(--navy) 0%, var(--grey) 100%); }
  .ornament-area.vertical-right { background: linear-gradient(90deg, var(--grey) 0%, var(--navy) 100%); }

  .wordmark {
    font-weight: 600;
    color: var(--navy);
    text-transform: uppercase;
    letter-spacing: 0.06em;
    white-space: nowrap;
  }

  /* Letterhead */
  .letterhead { width: 540px; height: 764px; }
  .letterhead .content { padding: 44px 48px; }
  .letterhead .top { display: flex; justify-content: space-between; align-items: flex-start; }
  .letterhead .wordmark { font-size: 17px; }
  .letterhead .ornament-area { left: 0; right: 0; bottom: 0; height: 120px; }
  .contact-block { font-size: 7.5px; line-height: 1.6; color: var(--muted); }
  .contact-block strong { color: var(--navy); font-weight: 600; }
  .letter-body { margin-top: 46px; font-size: 8.5px; line-height: 1.65; max-width: 430px; }
  .letter-body p { margin-bottom: 11px; }
  .letter-body .signoff { margin-top: 18px; }
  .letter-body .signer { margin-top: 26px; font-weight: 600; color: var(--navy); }
  .letter-body .signer-role { font-weight: 400; color: var(--muted); }

  /* Second sheet */
  .second-sheet { width: 540px; height: 764px; }
  .second-sheet .ornament-area { right: 0; top: 250px; bottom: 0; width: 110px; }
  .second-sheet .content { position: absolute; left: 0; right: 110px; top: 318px; text-align: center; }
  .second-sheet .wordmark { font-size: 28px; }

  /* Envelope */
  .envelope { width: 1040px; height: 452px; }
  .envelope .ornament-area { left: 0; top: 0; bottom: 0; width: 150px; }
  .envelope .content { padding: 40px 0 0 210px; }
  .envelope .wordmark { font-size: 20px; }
  .envelope .return-address { margin-top: 8px; font-size: 9px; color: var(--muted); }
  .stamp-box {
    position: absolute; top: 36px; right: 40px; z-index: 1;
    width: 84px; height: 96px;
    border: 1.5px solid var(--navy);
    display: flex; align-items: center; justify-content: center;
    text-align: center; font-size: 9px; line-height: 1.4; color: var(--muted);
    padding: 8px;
  }

  /* Business cards */
  .card { width: 510px; height: 291px; }
  .card-back .ornament-area { left: 0; right: 0; bottom: 0; height: 62px; }
  .card-back .content { padding: 36px 40px 0 40px; display: flex; justify-content: space-between; }
  .card-back .wordmark { font-size: 17px; }
  .person { margin-top: 30px; }
  .person .name { font-size: 18px; font-weight: 600; color: var(--navy); }
  .person .title { font-size: 10px; color: var(--muted); }
  .card-details { font-size: 9px; line-height: 1.75; color: var(--muted); margin-top: 4px; }
  .card-details strong { color: var(--navy); font-weight: 600; }
  .card-front .ornament-area { right: 0; top: 0; bottom: 0; width: 96px; }
  .card-front .content { position: absolute; left: 56px; top: 128px; }
  .card-front .wordmark { font-size: 22px; }
</style>
</head>
<body>

  <div class="row">
    <section class="piece letterhead" aria-label="Letterhead">
      <div class="ornament-area horizontal" role="img" aria-label="Decorative navy and grey wave ornament along the bottom edge"></div>
      <div class="content">
        <div class="top">
          <div class="wordmark">TM Halvorsen Law</div>
          <div class="contact-block">
            <strong>TM Halvorsen Law PLLC</strong><br>
            482 Linden Avenue, Suite 210<br>
            Raleigh, NC 27601<br>
            (555) 014-2290<br>
            tmhalvorsenlaw.com
          </div>
        </div>
        <div class="letter-body">
          <p>March 4, 2025</p>
          <p>Dear Ms. Carter,</p>
          <p>Thank you for meeting with our office to discuss your matter. This letter confirms the scope of our engagement and outlines the next steps we will take on your behalf.</p>
          <p>We will review the documents you provided, contact opposing counsel, and prepare a written summary of your options. Please keep copies of any new notices you receive and forward them to us promptly.</p>
          <p>Our fees are billed monthly as set out in the attached agreement. If you have questions at any time, please call or write, and we will respond within one business day.</p>
          <p class="signoff">Sincerely,</p>
          <p class="signer">Tessa M. Halvorsen<br><span class="signer-role">Attorney at Law</span></p>
        </div>
      </div>
    </section>

    <section class="piece second-sheet" aria-label="Second sheet">
      <div class="ornament-area vertical-right" role="img" aria-label="Decorative navy and grey wave ornament along the right edge"></div>
      <div class="content">
        <div class="wordmark">TM Halvorsen Law</div>
      </div>
    </section>
  </div>

  <section class="piece envelope" aria-label="Envelope">
    <div class="ornament-area vertical" role="img" aria-label="Decorative navy and grey wave ornament along the left edge"></div>
    <div class="content">
      <div class="wordmark">TM Halvorsen Law</div>
      <div class="return-address">482 Linden Avenue, Suite 210, Raleigh, NC 27601</div>
    </div>
    <div class="stamp-box">Place Stamp Here</div>
  </section>

  <div class="row">
    <section class="piece card card-back" aria-label="Business card, contact side">
      <div class="ornament-area horizontal" role="img" aria-label="Decorative navy and grey wave ornament along the bottom edge"></div>
      <div class="content">
        <div>
          <div class="wordmark">TM Halvorsen Law</div>
          <div class="person">
            <div class="name">Daniel Price</div>
            <div class="title">Advocate</div>
          </div>
        </div>
        <div class="card-details">
          <strong>TM Halvorsen Law PLLC</strong><br>
          482 Linden Avenue, Suite 210<br>
          Raleigh, NC 27601<br>
          (555) 014-2290<br>
          office@tmhalvorsenlaw.com<br>
          www.tmhalvorsenlaw.com
        </div>
      </div>
    </section>

    <section class="piece card card-front" aria-label="Business card, name side">
      <div class="ornament-area vertical-right" role="img" aria-label="Decorative navy and grey wave ornament along the right edge"></div>
      <div class="content">
        <div class="wordmark">TM Halvorsen Law</div>
      </div>
    </section>
  </div>

</body>
</html>
```